Gather the Orchard Gala Graphic Design

I’m seeking a professional graphic designer experienced in event branding to create a cohesive suite of materials for our third annual fundraising gala, “Gather the Orchard.” This year's theme is " An Evening in Linen to Gather the Orchard" Need to design collateral for website, social media and email blasts.
Target Market(s)
Affluent gala attendees
Industry/Entity Type
Fundraising / Charity / Outdoors / Sports
Font styles to use
Decorative
Script
Colors
0054AA
0677BA
7BADD7
CADEEF
E8F1F8
0094D4
00A9DD
6FCCEA
C7EBF8
E9F6FB
00AB8E
00BBA5
67D7C9
C6EFE9
E9F9F6
6B429C
8869AF
B7A5CE
E3DAEB
F3F0F8

```html
<!DOCTYPE html>
<html lang="en">
<head>
<meta charset="utf-8">
<title>An Evening in Linen to Gather the Orchard</title>
<link rel="stylesheet" href="https://fonts.googleapis.com/css2?family=Bebas+Neue&family=Great+Vibes&family=Poppins:wght@400;600;700&display=swap">
<style>
  :root {
    --ink-deep: #0a1b1f;
    --ink: #10292d;
    --ink-mid: #173b3f;
    --teal: #67d7c9;
    --teal-soft: #6fccea;
    --purple: #6b429c;
    --purple-soft: #8869af;
    --white: #ffffff;
    --amber: rgba(226, 160, 44, 0.55);
  }
  * { box-sizing: border-box; margin: 0; padding: 0; }
  html, body { width: 709px; height: 1200px; overflow: hidden; background: var(--ink-deep); }
  .flyer {
    position: relative; width: 709px; height: 1200px; overflow: hidden;
    font-family: "Poppins", sans-serif; color: var(--white);
  }
  .backdrop {
    position: absolute; inset: 0;
    background:
      radial-gradient(circle at 78% 20%, var(--amber) 0, rgba(226,160,44,0) 26%),
      radial-gradient(circle at 88% 45%, rgba(226,160,44,0.35) 0, rgba(226,160,44,0) 18%),
      radial-gradient(circle at 20% 88%, rgba(40,110,110,0.45) 0, rgba(40,110,110,0) 35%),
      linear-gradient(160deg, var(--ink-mid) 0%, var(--ink) 45%, var(--ink-deep) 100%);
  }
  .brand {
    position: absolute; left: 64px; top: 96px;
    display: flex; align-items: center; gap: 14px;
  }
  .brand-dot { width: 18px; height: 18px; border-radius: 50%; background: var(--white); }
  .brand-name {
    font-weight: 400; font-size: 21px; line-height: 1.05; text-transform: uppercase; color: var(--white);
  }
  .title-script {
    position: absolute; left: 62px; top: 262px;
    font-family: "Great Vibes", cursive; font-size: 84px; line-height: 1;
  }
  .title-main {
    position: absolute; left: 62px; top: 364px;
    font-family: "Bebas Neue", sans-serif; font-size: 98px; line-height: 0.9; letter-spacing: -0.5px;
  }
  .title-main .accent { color: var(--teal); display: block; }
  .rule { position: absolute; left: 64px; width: 98px; height: 2px; background: var(--teal); }
  .rule.top { top: 580px; }
  .rule.bottom { top: 718px; }
  .subtitle {
    position: absolute; left: 64px; top: 606px;
    font-weight: 600; font-size: 23px; line-height: 1.38; text-transform: uppercase;
  }
  .invite { position: absolute; left: 62px; top: 758px; display: flex; align-items: center; gap: 18px; }
  .invite-script { font-family: "Great Vibes", cursive; font-size: 54px; color: var(--teal); line-height: 1; }
  .invite-text { font-size: 15px; line-height: 1.3; width: 330px; }
  .cta {
    position: absolute; left: 62px; top: 852px; width: 396px; height: 30px;
    background: var(--purple); border-radius: 15px;
    font-size: 21px; line-height: 30px; padding-left: 28px; text-transform: uppercase; letter-spacing: 0.3px;
  }
  .cta strong { font-weight: 700; }
  .detail { position: absolute; top: 918px; font-size: 15px; line-height: 1.35; text-transform: uppercase; }
  .detail.when { left: 62px; }
  .detail.where { left: 350px; }
  .detail-label {
    display: inline-block; background: var(--teal); color: var(--ink-deep);
    font-weight: 700; font-size: 14px; padding: 0 22px; border-radius: 10px; line-height: 20px; margin-bottom: 8px;
  }
  .detail .highlight { color: var(--teal); font-weight: 700; }
  .notice {
    position: absolute; left: 62px; top: 1033px; width: 560px; height: 28px;
    display: flex; align-items: center;
  }
  .notice-band {
    position: absolute; left: 14px; top: 2px; right: 0; height: 24px;
    background: linear-gradient(90deg, var(--purple) 0%, rgba(107,66,156,0.6) 55%, rgba(107,66,156,0) 100%);
  }
  .notice svg { position: relative; z-index: 1; }
  .notice-text {
    position: relative; z-index: 1; margin-left: 8px;
    font-weight: 700; font-size: 18px; text-transform: uppercase; color: var(--white);
  }
  .site {
    position: absolute; left: 59px; top: 1122px;
    font-size: 16px; letter-spacing: 3.4px; text-transform: uppercase;
  }
  .site .accent { color: var(--teal); }
</style>
</head>
<body>
<main class="flyer">
  <div class="backdrop" role="img" aria-label="Dark teal marbled backdrop with soft golden bokeh lights"></div>

  <div class="brand">
    <span class="brand-dot"></span>
    <span class="brand-name">Save<br>Harrow Point<br>Orchard</span>
  </div>

  <h1>
    <span class="title-script">An Evening in</span>
    <span class="title-main">Linen to Gather<span class="accent">The Orchard</span></span>
  </h1>

  <div class="rule top"></div>
  <p class="subtitle">A fundraising gala in celebration<br>of the 152th anniversary of<br>Harrow Point Orchard</p>
  <div class="rule bottom"></div>

  <div class="invite">
    <span class="invite-script">Join us</span>
    <p class="invite-text">For a luminous evening of dining, delectable libations, live entertainment, artistry and more!</p>
  </div>

  <div class="cta">Get your <strong>tickets today!</strong></div>

  <div class="detail when">
    <span class="detail-label">When</span><br>
    <span class="highlight">November 18th,</span> 2025<br>
    Cocktails 6:00PM<br>
    VIP ticket holders 5:00PM
  </div>
  <div class="detail where">
    <span class="detail-label">Where</span><br>
    Linden Cove - 4820<br>
    Orchard Ridge Rd<br>
    Fairhaven
  </div>

  <div class="notice">
    <div class="notice-band"></div>
    <svg width="24" height="30" viewBox="0 0 24 30" aria-hidden="true">
      <path d="M12 1C6 1 1.5 5.5 1.5 11.3 1.5 19 12 29 12 29s10.5-10 10.5-17.7C22.5 5.5 18 1 12 1z" fill="#67d7c9"/>
      <circle cx="12" cy="11" r="4.2" fill="#10292d"/>
    </svg>
    <span class="notice-text">Cocktail attire space is limited</span>
  </div>

  <p class="site">www.<span class="accent">saveharrowpointorchard</span>.org</p>
</main>
</body>
</html>
```